Therapy Dog Business need a brochure

I need a brochure designed for my Canine Assisted Therapy business in Victoria Australia. I have a logo already and info and photos to upload.
Best as white background and using the colours from the logo please
Updates

Hi Everyone,
I am sorry to have to revise the brief. I have added three new photos I was unable to add due to the size. I have had to wait for my photographer to change the size to add them today. I have been really inspired by all the work you have done so far. Thank you.
Could you please add the following on the brochure. (Under the individual dogs photo)
1. Pebble is the white dog. Please add the following under her picture. Pebble is one of the first Court Dogs in Australia. Working in Victoria, she has worked in the following Courts. The Inquest Tribunal of Norvale, The Petty Sessions Bench in Collingwood, and the Shire Tribunal in Melbourne CBD. Her ability to use her intuition for clients is inspiring. Please contact us for potential use in Courts. Pebble has worked at the Halden Constabulary College, and at KESTREL at Hal Con. She is a stunning dog!
2. Tobias is the golden dog. Tobias is Pebbles son, and had her instinct of intuition of who needs his help. Tobias has an incredible soft approach as does his mother Pebble. He is incredibly safe with young children, and yet has a playful nature for adolescents and adults alike. He is soft and caring, and like his mother will go to those who need him most. Tobias like his mother has worked at Halden Constabulary, his time at HC included the Halden Constabulary Command (HCC) Both he and his mother have very impressive CV'S!
3. Clover the black dog. Clover is my Therapy and Assistance dog "trainer" she is safe and stable with all the dogs and people I train for Therapy Dog Training and Assistance Dog Training. She has also been with me on my journey as a Counsellor and I have been able to work alongside her and Pebble for Counselling sessions.
She is soft, caring, and also intuitive. I am incredibly grateful for her help, as well as Pebble and Tobias.
ALSO I am so sorry to add this but could you also add the following: Maybe in dot point?
Court Dog Availability
Therapy Dog Visits - Lawyers - Courts - Child Protection
Police Station / Ambulance Station / Fire Station - Visits
Private Therapy Dog Sessions
website and email confirmation coming soon. Thank you

Target Market(s)

First Responders

Requirements
Must have
• All the photos provided.
Should not have
• Generic photos

```html
<!DOCTYPE html>
<html lang="en">
<head>
<meta charset="utf-8">
<title>Canine Assisted Therapy Brochure</title>
<link rel="stylesheet" href="https://fonts.googleapis.com/css2?family=Poppins:wght@400;500;600;700&family=Lilita+One&family=Dancing+Script:wght@600&display=swap">
<style>
:root{
  --bg:#e9ecec;
  --paper:#ffffff;
  --pink:#e07d7c;
  --pink-soft:#f3c9c4;
  --maroon:#8a2b22;
  --orange:#e9a066;
  --orange-soft:#f6d2ad;
  --ink:#1d1d1d;
  --text:#333333;
  --line:#d9d9d9;
  --photo-a:#c9a27a;
  --photo-b:#7f8fc9;
}
*{box-sizing:border-box;margin:0;padding:0}
html,body{width:1200px;height:2400px;overflow:hidden;background:var(--bg)}
body{position:relative;font-family:'Poppins',sans-serif;color:var(--text)}
.spread{position:absolute;left:40px;width:1120px;height:860px;background:var(--paper);box-shadow:0 10px 30px rgba(0,0,0,.15);overflow:hidden}
.spread--outer{top:280px}
.spread--inner{top:1260px}
.panel{position:absolute;top:0;width:373.33px;height:860px}
.panel--1{left:0}.panel--2{left:373.33px}.panel--3{left:746.66px}
.abs{position:absolute}
.blob{position:absolute;top:0}
.panel-heading{position:absolute;left:42px;top:42px;color:#fff;font-weight:600;font-size:21px;line-height:1.2}
.body-copy{font-size:12.5px;line-height:1.3;color:var(--text)}
.photo{position:absolute;overflow:hidden}
.brand{position:absolute;display:flex;align-items:center;gap:8px;left:0;right:0;justify-content:center}
.brand__dot{width:26px;height:26px;border-radius:50%;background:var(--pink)}
.brand__name{font-family:'Poppins',sans-serif;font-weight:600;color:var(--maroon);font-size:17px}
.pill{position:absolute;left:50%;transform:translateX(-50%);border-radius:6px;color:#fff;text-align:center;white-space:nowrap}
.pill--web{background:var(--maroon);font-weight:600;letter-spacing:2px;font-size:15px;padding:5px 18px;width:280px}
.pill--pink{background:var(--pink);font-weight:600;font-size:17px;padding:3px 22px;width:275px}
.service{position:absolute;left:40px;display:flex;align-items:center;gap:14px;font-weight:600;font-size:16px;color:var(--ink)}
.service__icon{width:46px;height:46px;border-radius:50%;background:var(--orange-soft);display:flex;align-items:center;justify-content:center}
.service__icon span{width:26px;height:26px;border-radius:50%;background:var(--orange)}
.rule{position:absolute;left:40px;width:300px;height:1px;background:var(--line)}
.bullets{position:absolute;list-style:none;font-size:12.5px;line-height:1.55}
.bullets li{display:flex;align-items:center;gap:10px}
.bullets li::before{content:"";width:9px;height:9px;border-radius:50%;background:var(--maroon)}
.center{position:absolute;left:0;right:0;text-align:center}
.contact-icon{position:absolute;left:50%;transform:translateX(-50%)}
.title-display{font-family:'Lilita One',sans-serif;line-height:1;letter-spacing:1px}
.benefit{position:absolute;left:36px;display:flex;gap:14px;width:312px}
.benefit__icon{flex:0 0 44px;height:44px;border-radius:50%;border:3px solid var(--pink-soft);background:#fff;display:flex;align-items:center;justify-content:center}
.benefit__icon span{width:28px;height:28px;border-radius:50%;background:var(--pink)}
.benefit__title{font-weight:600;color:var(--maroon);font-size:13px}
.benefit .body-copy{font-size:11.5px;line-height:1.3}
.why{position:absolute;left:36px;display:flex;gap:18px;width:310px}
.why__icon{flex:0 0 44px;height:44px;position:relative}
.why__title{font-weight:600;color:var(--ink);font-size:12px}
.why .body-copy{font-size:11.5px;line-height:1.28}
.dog-label{position:absolute;background:var(--pink);color:#fff;font-weight:600;font-size:14.5px;padding:3px 12px;border-radius:4px}
.dog-copy{position:absolute;font-size:11.5px;line-height:1.3;width:310px}
</style>
</head>
<body>

<!-- OUTER SPREAD -->
<section class="spread spread--outer">
  <!-- panel 1 -->
  <div class="panel panel--1">
    <svg class="blob" width="373" height="140" viewBox="0 0 373 140"><path d="M0 0H373C350 10 320 20 300 40C280 70 260 90 200 100C130 110 60 105 0 140Z" fill="var(--pink)"/></svg>
    <h2 class="panel-heading">What is Canine<br>Assisted Therapy?</h2>
    <p class="abs body-copy" style="left:40px;top:132px;width:295px;font-size:12.8px">Canine Assisted Therapy (CAT) is a unique form of therapy that integrates trained therapy dogs into the healing process. By working alongside licensed therapists, these compassionate and well-trained dogs help support individuals in overcoming emotional, physical, and psychological challenges. This innovative approach promotes healing, reduces stress, and enhances overall well-being.</p>
    <div class="service" style="top:302px"><div class="service__icon"><span></span></div>Court Dog Availability</div>
    <div class="rule" style="top:356px"></div>
    <div class="service" style="top:368px"><div class="service__icon"><span></span></div>Therapy Dog Visits</div>
    <ul class="bullets" style="left:42px;top:420px"><li>Lawyers</li><li>Courts</li><li>Child Protection</li></ul>
    <ul class="bullets" style="left:200px;top:420px"><li>Police Station</li><li>Ambulance Station</li><li>Fire Station</li></ul>
    <div class="rule" style="top:488px"></div>
    <div class="service" style="top:502px;line-height:1.2"><div class="service__icon"><span></span></div>Private Therapy<br>Dog Sessions</div>
    <svg class="photo" style="left:0;top:590px" width="373" height="270" viewBox="0 0 373 270" role="img" aria-label="Photo of a woman grooming a golden dog">
      <defs><linearGradient id="g1" x1="0" y1="0" x2="1" y2="1"><stop offset="0" stop-color="#efe6dc"/><stop offset="1" stop-color="var(--photo-a)"/></linearGradient></defs>
      <path d="M0 40C40 0 110 -5 160 20L373 20V270H0Z" fill="url(#g1)"/>
      <path d="M60 40C100 5 170 5 210 30" stroke="var(--orange)" stroke-width="10" fill="none"/>
    </svg>
  </div>

  <!-- panel 2 -->
  <div class="panel panel--2">
    <div class="brand" style="top:78px"><span class="brand__dot"></span><span class="brand__name">Kindred Tails</span></div>
    <svg class="photo" style="left:100px;top:145px" width="190" height="160" viewBox="0 0 190 160" role="img" aria-label="Photo of a black and white puppy beside a pink heart">
      <path d="M95 30C95 0 60 -5 50 20C40 -5 5 0 5 30C5 60 50 90 50 90" fill="none"/>
      <path d="M120 10C150 -5 185 15 180 50C175 90 130 120 110 140L110 10Z" fill="var(--pink)"/>
      <rect x="20" y="30" width="110" height="130" rx="40" fill="#5a5a5a"/>
    </svg>
    <div class="center" style="top:340px;color:var(--orange);font-weight:500;font-size:23px;letter-spacing:.5px">JOIN THE HEALING</div>
    <div class="center" style="top:360px;color:var(--maroon);font-family:'Dancing Script',cursive;font-size:32px">Journey Today</div>
    <p class="center body-copy" style="top:408px;padding:0 42px;font-size:12.5px">Whether you are seeking emotional support or mental health improvement, Canine Assisted Therapy offers a unique &amp; compassionate approach to healing.</p>
    <div class="pill pill--pink" style="top:480px">Connect with us today</div>
    <p class="center body-copy" style="top:532px;padding:0 40px;font-weight:500;font-size:13px;color:var(--ink)">To learn more about how a therapy dog can help enhance your life and well-being.</p>
    <svg class="contact-icon" style="top:585px" width="22" height="22" viewBox="0 0 22 22"><circle cx="11" cy="11" r="10" fill="none" stroke="var(--pink)" stroke-width="1.5"/><path d="M11 5a4 4 0 0 1 4 4c0 3-4 7-4 7s-4-4-4-7a4 4 0 0 1 4-4z" fill="var(--pink)"/><circle cx="11" cy="9" r="1.4" fill="#fff"/></svg>
    <p class="center" style="top:612px;font-size:14px;line-height:1.3;color:var(--ink)">20973 Lorem Ipsum<br>Lorem Ipsum 777111</p>
    <svg class="contact-icon" style="top:678px" width="22" height="22" viewBox="0 0 22 22"><circle cx="11" cy="11" r="10" fill="none" stroke="var(--pink)" stroke-width="1.5"/><path d="M7 6l2 0 1 3-1.3 1a6 6 0 0 0 3.3 3.3l1-1.3 3 1v2c0 .6-.5 1-1 1A9 9 0 0 1 6 7c0-.5.4-1 1-1z" fill="var(--pink)"/></svg>
    <p class="center" style="top:712px;font-size:14px;color:var(--ink)">0400 123 456</p>
    <svg class="contact-icon" style="top:742px" width="22" height="22" viewBox="0 0 22 22"><circle cx="11" cy="11" r="10" fill="none" stroke="var(--pink)" stroke-width="1.5"/><rect x="6" y="7.5" width="10" height="7" rx="1" fill="var(--pink)"/><path d="M6 8l5 4 5-4" stroke="#fff" fill="none"/></svg>
    <p class="center" style="top:768px;font-size:14px;color:var(--ink)">hello@kindredtails.example</p>
    <div class="pill pill--web" style="top:800px">www.kindredtails.example</div>
  </div>

  <!-- panel 3 -->
  <div class="panel panel--3">
    <svg class="blob" style="left:253px" width="120" height="260" viewBox="0 0 120 260"><path d="M30 0H120V260C100 230 60 220 40 180C20 140 60 110 40 70C25 45 10 25 30 0Z" fill="var(--pink)"/></svg>
    <div class="brand" style="top:90px"><span class="brand__dot"></span><span class="brand__name">Kindred Tails</span></div>
    <svg class="photo" style="left:0;top:185px" width="373" height="350" viewBox="0 0 373 350" role="img" aria-label="Photo of a black dog and a golden dog side by side">
      <path d="M30 150C20 60 80 20 150 10C230 0 330 40 340 140C350 240 300 340 180 345C70 350 40 250 30 150Z" fill="var(--orange)"/>
      <path d="M10 200C10 120 60 90 110 90C170 90 190 150 190 230L190 350H30Z" fill="#2b2b2b"/>
      <path d="M170 110C170 50 220 30 270 40C330 50 360 110 360 200L360 330H180Z" fill="#d49a52"/>
    </svg>
    <div class="center title-display" style="top:545px;font-size:42px;color:var(--ink)">CANINE</div>
    <div class="center title-display" style="top:587px;font-size:46px;color:var(--orange)">ASSISTED</div>
    <div class="center title-display" style="top:633px;font-size:42px;color:var(--ink)">THERAPY</div>
    <div class="center" style="top:680px;color:var(--pink);font-weight:600;font-size:19px">IN VICTORIA AUSTRALIA</div>
    <div class="abs" style="left:162px;top:712px;width:50px;height:3px;background:var(--ink)"></div>
    <p class="center" style="top:728px;font-size:12.5px;font-weight:500;line-height:1.3;padding:0 30px;color:var(--ink)">Is a unique form of therapy that integrates trained therapy dogs into the healing process.</p>
    <div class="pill pill--web" style="top:800px">www.kindredtails.example</div>
  </div>
</section>

<!-- INNER SPREAD -->
<section class="spread spread--inner">
  <!-- panel 1 -->
  <div class="panel panel--1">
    <svg class="blob" width="373" height="125" viewBox="0 0 373 125"><path d="M0 0H373C355 20 340 50 320 70C290 100 220 95 160 98C90 100 40 100 0 125Z" fill="var(--pink)"/></svg>
    <h2 class="panel-heading" style="left:38px;top:46px">Benefits of Canine<br>Assisted Therapy</h2>
    <div class="benefit" style="top:140px"><div class="benefit__icon"><span></span></div><div><div class="benefit__title">Emotional Support and Comfort</div><p class="body-copy">Therapy dogs provide immediate emotional support, offering comfort and companionship during therapy sessions. Their calming presence helps reduce feelings of anxiety, stress, and depression, and grief, creating a safe and nurturing environment for healing.</p></div></div>
    <div class="rule" style="top:268px;left:36px"></div>
    <div class="benefit" style="top:282px"><div class="benefit__icon"><span></span></div><div><div class="benefit__title">Stress Relief and Relaxation</div><p class="body-copy">Interacting with dogs has been proven to reduce cortisol (stress hormone) levels and increase serotonin and oxytocin, the "feel-good" hormones. This natural relief from stress makes Canine Assisted Therapy an ideal option for individuals dealing with anxiety, trauma, PTSD, and grief.</p></div></div>
    <div class="rule" style="top:424px;left:36px"></div>
    <div class="benefit" style="top:440px"><div class="benefit__icon"><span></span></div><div><div class="benefit__title">Improved Mental Health</div><p class="body-copy">Therapy dogs encourage social interaction, communication, and emotional expression, helping individuals address mental health challenges such as depression, anxiety, PTSD, and grief. The unconditional love and companionship of a dog can foster trust and openness during therapy sessions.</p></div></div>
    <svg class="photo" style="left:0;top:600px" width="373" height="260" viewBox="0 0 373 260" role="img" aria-label="Photo of three dogs resting on a blue sofa against a brick wall">
      <defs><linearGradient id="g2" x1="0" y1="0" x2="0" y2="1"><stop offset="0" stop-color="#b7805f"/><stop offset=".55" stop-color="#c49a7c"/><stop offset=".56" stop-color="var(--photo-b)"/><stop offset="1" stop-color="#6f80bf"/></linearGradient></defs>
      <path d="M0 30C60 0 110 10 160 30C220 50 260 25 300 15L373 15V260H0Z" fill="url(#g2)"/>
      <path d="M0 22C60 -8 110 2 160 22C220 42 260 17 300 7" stroke="var(--maroon)" stroke-width="9" fill="none"/>
    </svg>
  </div>

  <!-- panel 2 -->
  <div class="panel panel--2">
    <h2 class="abs" style="left:36px;top:42px;font-weight:600;font-size:24px;line-height:1.2;color:var(--ink)">Why ChooseCanine<br><span style="color:var(--maroon)">Assisted Therapy?</span></h2>
    <div class="why" style="top:128px"><div class="why__icon"><svg width="44" height="44" viewBox="0 0 44 44" role="img" aria-label="Small dog icon with a heart"><path d="M10 4c2-3 6-1 5 2-1 2-5 5-5 5s-4-3-5-5c-1-3 3-5 5-2z" fill="var(--pink)"/><rect x="14" y="16" width="22" height="26" rx="8" fill="var(--ink)"/></svg></div><div><div class="why__title">Proven Effectiveness:</div><p class="body-copy">Studies and testimonials highlight the positive effects therapy dogs have on emotional, psychological and physical health.</p></div></div>
    <div class="rule" style="top:205px;left:36px;width:310px;border-top:1px dashed #bbb;background:none"></div>
    <div class="why" style="top:218px"><div class="why__icon"><svg width="44" height="44" viewBox="0 0 44 44" role="img" aria-label="Small dog house icon"><path d="M4 20L22 4 40 20" stroke="var(--pink)" stroke-width="4" fill="none"/><rect x="10" y="20" width="24" height="20" fill="var(--ink)"/></svg></div><div><div class="why__title">Non-Invasive and Gentle</div><p class="body-copy">Therapy dogs provide a natural and non-threatening way to engage with patients, making it accessible for individuals who may feel apprehensive about traditional therapy methods.</p></div></div>
    <div class="rule" style="top:310px;left:36px;width:310px;border-top:1px dashed #bbb;background:none"></div>
    <div class="why" style="top:322px"><div class="why__icon"><svg width="44" height="44" viewBox="0 0 44 44" role="img" aria-label="Small dog icon"><circle cx="22" cy="8" r="5" fill="none" stroke="var(--pink)" stroke-width="2"/><rect x="8" y="18" width="28" height="22" rx="8" fill="var(--ink)"/></svg></div><div><div class="why__title">Safe and Trustworthy</div><p class="body-copy">All therapy dogs are carefully trained to work with professionals, ensuring that interactions are safe, beneficial, and appropriate for all individuals.</p></div></div>
    <svg class="photo" style="left:28px;top:418px" width="320" height="215" viewBox="0 0 320 215" role="img" aria-label="Photo of Pebble the white dog lying on a blue cushion">
      <path d="M20 120C10 60 60 10 130 5C200 0 250 40 260 90C300 100 320 150 290 185C250 215 60 215 30 185C10 165 10 140 20 120Z" fill="var(--photo-b)" stroke="var(--orange)" stroke-width="4"/>
      <ellipse cx="160" cy="120" rx="80" ry="55" fill="#efe5d6"/>
    </svg>
    <div class="dog-label" style="left:36px;top:648px">Pebble is the white dog</div>
    <p class="dog-copy" style="left:36px;top:688px">Please add the following under her picture. Pebble is one of the first Court Dogs in Australia. Working in Victoria, she has worked in the following Courts. The Inquest Tribunal of Norvale, The Petty Sessions Bench in Collingwood, and the Shire Tribunal in Melbourne CBD. Her ability to use her intuition for clients is inspiring. Please contact us for potential use in Courts. Pebble has worked at the Halden Constabulary College, and at KESTREL at Hal Con. She is a stunning dog!</p>
  </div>

  <!-- panel 3 -->
  <div class="panel panel--3">
    <svg class="blob" style="left:290px" width="83" height="100" viewBox="0 0 83 100"><path d="M10 0H83V100C60 95 40 80 25 60C10 40 0 20 10 0Z" fill="var(--pink)"/></svg>
    <svg class="photo" style="left:20px;top:40px" width="330" height="215" viewBox="0 0 330 215" role="img" aria-label="Photo of Tobias the golden dog lying on a blue cushion">
      <path d="M20 120C20 60 80 10 160 8C240 5 300 50 310 110C320 170 280 205 180 208C80 210 20 180 20 120Z" fill="var(--photo-b)" stroke="var(--orange)" stroke-width="4"/>
      <ellipse cx="150" cy="110" rx="95" ry="55" fill="#dcb98a"/>
    </svg>
    <div class="dog-label" style="left:30px;top:262px">Tobias is the golden dog</div>
    <p class="dog-copy" style="left:30px;top:302px">Tobias is Pebbles son, and had her instinct of intuition of who needs his help. Tobias has an incredible soft approach as does his mother Pebble. He is incredibly safe with young children, and yet has a playful nature for adolescents and adults alike. He is soft and caring, and like his mother will go to those who need him most. Tobias like his mother has worked at Halden Constabulary, his time at HC included the Halden Constabulary Command (HCC) Both he and his mother have very impressive CV'S!</p>
    <svg class="photo" style="left:0;top:468px" width="350" height="180" viewBox="0 0 350 180" role="img" aria-label="Photo of Clover the black dog lying on a blue cushion">
      <path d="M30 100C30 40 100 5 170 5C250 5 320 40 325 100C330 160 280 175 170 176C70 177 30 160 30 100Z" fill="var(--photo-b)" stroke="var(--orange)" stroke-width="4"/>
      <ellipse cx="170" cy="110" rx="110" ry="45" fill="#1f1f1f"/>
    </svg>
    <div class="dog-label" style="left:30px;top:662px">Clover the black dog</div>
    <p class="dog-copy" style="left:30px;top:700px">Clover is my Therapy and Assistance dog "trainer" she is safe and stable with all the dogs and people I train for Therapy Dog Training and Assistance Dog Training. She has also been with me on my journey as a Counsellor and I have been able to work alongside her and Pebble for Counselling sessions. She is soft, caring, and also intuitive. I am incredibly grateful for her help, as well as Pebble and Tobias.</p>
  </div>
</section>

</body>
</html>
```